Suchen ansprechendes & seriöses Urkunden/Zertifikat Design für Webseite & Druck
Zielgruppe
Auf unserer Webseite http://rege-im-alter-netz.de können sich Unternehmen, Institutionen und Vereine ihre Seniorenfreundlichkeit durch ein Zertifikat bestätigen und zertifizieren lassen.
Unsere Kundengruppen: Hotel – Gastronomie – Wellness – Reisen und Touristik – Touristikregionen – Seniorenshop – Onlineshop – Unternehmen als Dienstleister – Medizin und Health-Service – Apotheke – Altenheim – Pflegeheim – Seniorenheim – Vereine – Seniorenservice – Zahnärzte – Fitnessstudio – Sportstudio – Physiotherapie – Sportverein – Golfclub – und viele weitere seniorenfreundliche Institutionen.
Aufgabenstellung
Auftrag- Ausschreibung:
- Erstellung eines Design:
- Urkunde für Webseite rege-im-alter-netz.de - Das Zertifikat "Rege im Alter“
Funktion:
Kunde erkennt das Zertifikat - Logo auf einer Webseite und Klickt auf dieses.
Er wird weitergeleitet auf eine Unterseite, worin die Richtlinien und die Urkunde sichtbar wird.
Zielgruppe:
- Unternehmen, welche das Zertifikat auf Ihre Webseite setzen. Die Urkunde gibt Auskunft, dass der Dienstleister einen besonderen Service für Senioren ausübt. Die Urkunde ist sichtbar auf der Webseite, indem das Logo angeklickt wird. Die Urkunde gibt es ebenfalls als Download, damit der Kunde diese in seinen Geschäftsräumen aufhängen kann oder diese in seinen Werbeunterlagen präsentieren kann.
- Verbraucher sollen beeindruckt sein, von der Urkunde, welches Vertrauen ausstrahlt, aber auch Seriosität
Folgende Ausstrahlung soll die Urkunde haben:
- Soll Mitbewerber des Zertifikatsinhaber beeindrucken und das Verlangen aufzeigen, sich ebenfalls zertifizieren zu lassen ( ca: 70% der Kunden sind Mitbewerber … ). Nach dem Motto "Das Logo ist super und edel, das muss ich auch haben!"
- Der Kunde als Verbraucher soll Vertrauen gewinnen, die Daten sollen gut sichtbar sein, aber nicht verkitscht wie eine Urkunde bei einer Kaffeefahrt. Der Verbraucher geht auf das Zertifikat und kommt zur Urkunde, deshalb soll die Farbe, und Darstellung, Seriosität des Unternehmens ausstrahlen.
Sonstiges
- Die Urkunde soll dem neuen Design unserer Seite (zu sehen unter: http://guetesiegel-welt.de) angepasst sein.
- Vor Auftragsendvergabe erhalten Sie noch ein telefonisches Briefing über unsere Erfahrungswerte
Link zur bestehenden alten Webseite (Altes Design): http://rege-im-alter-netz.de
Info Verbraucher: http://www.rege-im-alter-netz.de/verbraucher/
Info zum Zertifikat: http://www.rege-im-alter-ne..

```html
<!DOCTYPE html>
<html lang="de">
<head>
<meta charset="utf-8">
<title>Zertifikat – Rege im Alter</title>
<link href="https://fonts.googleapis.com/css2?family=Raleway:wght@200;400;600;700&display=swap" rel="stylesheet">
<style>
  :root {
    --paper-light: #f6f1e9;
    --paper-mid: #ebe1d2;
    --paper-edge: #d6c6ae;
    --frame: #b9a582;
    --frame-dark: #9a8564;
    --heading: #6e5a43;
    --label: #7a6448;
    --value: #3b3834;
    --seal: #c9c2b8;
    --seal-ring: #a9a195;
    --signature: #d2c4ae;
  }
  html, body {
    margin: 0;
    padding: 0;
    overflow: hidden;
    background: #ffffff;
  }
  .certificate {
    position: relative;
    width: 850px;
    height: 1200px;
    overflow: hidden;
    font-family: "Raleway", Arial, sans-serif;
    background:
      radial-gradient(ellipse at 50% 45%, var(--paper-light) 0%, var(--paper-mid) 60%, var(--paper-edge) 100%);
  }
  .frame {
    position: absolute;
    inset: 0;
  }
  .title {
    position: absolute;
    top: 84px;
    left: 0;
    width: 850px;
    margin: 0;
    text-align: center;
    font-weight: 200;
    font-size: 114px;
    line-height: 1;
    letter-spacing: 1px;
    color: var(--heading);
    white-space: nowrap;
  }
  .subtitle {
    position: absolute;
    top: 206px;
    left: 0;
    width: 850px;
    margin: 0;
    text-align: center;
    font-weight: 700;
    font-size: 44px;
    line-height: 1.1;
    letter-spacing: 0.5px;
    color: var(--heading);
  }
  .field {
    position: absolute;
    left: 0;
    display: grid;
    grid-template-columns: 312px 1fr;
    column-gap: 13px;
    font-size: 22px;
    line-height: 31.5px;
  }
  .field-label {
    text-align: right;
    font-weight: 600;
    color: var(--label);
  }
  .field-value {
    font-weight: 400;
    color: var(--value);
  }
  .field-id { top: 316px; }
  .field-provider { top: 386px; }
  .field-status { top: 536px; }
  .field-company { top: 594px; }
  .field-representative { top: 786px; }
  .field-first-check { top: 891px; }
  .field-valid { top: 932px; }
  .field-confirmed { top: 1052px; }
  .field-date .field-label,
  .field-date .field-value { font-size: 23px; }
  .signatures {
    position: absolute;
    top: 990px;
    left: 300px;
    width: 320px;
    height: 68px;
    background: linear-gradient(90deg, transparent, var(--signature) 30%, var(--signature) 70%, transparent);
    opacity: 0.55;
  }
  .signer {
    position: absolute;
    top: 1058px;
    font-size: 18px;
    line-height: 24px;
    color: var(--value);
  }
  .signer-first { left: 332px; }
  .signer-second { left: 465px; }
  .seal {
    position: absolute;
    top: 835px;
    left: 498px;
    width: 230px;
    height: 190px;
  }
  .page-number {
    position: absolute;
    left: 0;
    bottom: 0;
    padding: 4px 6px;
    font-size: 20px;
    font-weight: 600;
    color: var(--value);
    background: #ffffff;
  }
</style>
</head>
<body>
<main class="certificate">
  <svg class="frame" width="850" height="1200" viewBox="0 0 850 1200" aria-hidden="true">
    <g stroke="var(--frame)" fill="none">
      <line x1="70" y1="62" x2="780" y2="62" stroke-width="1.5"/>
      <line x1="70" y1="68" x2="780" y2="68" stroke-width="3"/>
      <line x1="70" y1="1116" x2="780" y2="1116" stroke-width="3"/>
      <line x1="70" y1="1122" x2="780" y2="1122" stroke-width="1.5"/>
      <line x1="72" y1="130" x2="72" y2="1100" stroke-width="1.5"/>
      <line x1="778" y1="130" x2="778" y2="1100" stroke-width="1.5"/>
      <line x1="72" y1="80" x2="72" y2="118" stroke-width="4" stroke-dasharray="1 3"/>
      <line x1="778" y1="80" x2="778" y2="118" stroke-width="4" stroke-dasharray="1 3"/>
      <line x1="72" y1="1102" x2="72" y2="1112" stroke-width="4" stroke-dasharray="1 3"/>
      <line x1="778" y1="1102" x2="778" y2="1112" stroke-width="4" stroke-dasharray="1 3"/>
    </g>
    <g fill="var(--frame-dark)">
      <rect x="419" y="59" width="12" height="12" transform="rotate(45 425 65)"/>
      <rect x="419" y="1113" width="12" height="12" transform="rotate(45 425 1119)"/>
    </g>
  </svg>

  <h1 class="title">ZERTIFIKAT</h1>
  <p class="subtitle">REGE IM ALTER</p>

  <div class="field field-id">
    <span class="field-label">Zertifikat ID:</span>
    <span class="field-value">7250441e9e</span>
  </div>

  <div class="field field-provider">
    <span class="field-label">Anbieter:</span>
    <span class="field-value">Rege im Alter<br>Ihr Zertifizierungsdienst<br>Zeile 3<br>Zeile 4</span>
  </div>

  <div class="field field-status">
    <span class="field-label">Status:</span>
    <span class="field-value">aktiv</span>
  </div>

  <div class="field field-company">
    <span class="field-label">Unternehmen:</span>
    <span class="field-value">Senioren Service Lindhof<br>Auenweg 8<br>12345 Stadt<br>Deutschland<br>info@lindhof.org</span>
  </div>

  <div class="field field-representative">
    <span class="field-label">Vertretungs-<br>berechtigter:</span>
    <span class="field-value">Frau Greta<br>Lindhof</span>
  </div>

  <div class="field field-date field-first-check">
    <span class="field-label">Erstprüfung am:</span>
    <span class="field-value">07.04.2017</span>
  </div>

  <div class="field field-date field-valid">
    <span class="field-label">gültig bis:</span>
    <span class="field-value">07.04.2019</span>
  </div>

  <div class="signatures" role="img" aria-label="Handschriftliche Unterschriften der Prüfer"></div>

  <div class="field field-date field-confirmed">
    <span class="field-label">Bestätigt von:</span>
    <span class="field-value"></span>
  </div>
  <span class="signer signer-first">K. Albers</span>
  <span class="signer signer-second">T. Wendel</span>

  <svg class="seal" viewBox="0 0 230 190" role="img" aria-label="Prüfsiegel">
    <path d="M120 110 L205 150 L215 185 L180 170 L150 150 Z" fill="var(--seal-ring)"/>
    <circle cx="94" cy="94" r="88" fill="var(--seal)" stroke="var(--seal-ring)" stroke-width="6"/>
  </svg>

  <span class="page-number">31</span>
</main>
</body>
</html>
```